Tormelli Welding and Fabrication LLC service truck wrap design

Need an eye catching design for a 2024 Vask crew cab 3500, cab only for Tormelli Welding and Fabrication LLC, relating to a metal working industry. We offer residential handrail fabrication and installation, commercial structural and repair. Please include the company’s logo (can be altered) that will be visible and comprehensible from 50ft away.
Updates

Designs look the same

Target Market(s)

Residential and commercial customers

Industry/Entity Type

Welding and fabrication

Requirements
Must have
• Logo and phone number
Nice to have
• Images involving metal or welding and fabrication

```html
<!DOCTYPE html>
<html lang="en">
<head>
<meta charset="utf-8">
<title>Tormelli Welding and Fabrication LLC – Cab Wrap</title>
<link href="https://fonts.googleapis.com/css2?family=Stardos+Stencil:wght@700&display=swap" rel="stylesheet">
<style>
  :root {
    --wrap-black: #050505;
    --accent-orange: #e2501a;
    --stripe-white: #ffffff;
    --cut-line: #d4161b;
    --paper: #ffffff;
    --text-light: #eef0f2;
    --spark-hot: #ffd9a0;
    --spark-warm: #c77a2e;
  }
  html, body {
    margin: 0;
    padding: 0;
    width: 896px;
    height: 1200px;
    overflow: hidden;
    background: var(--paper);
  }
  .wrap-canvas {
    position: relative;
    width: 896px;
    height: 1200px;
    display: flex;
    align-items: center;
    justify-content: center;
  }
  .cab-template {
    width: 860px;
    height: auto;
    display: block;
  }
  .brand-name {
    font-family: "Stardos Stencil", "Arial Black", sans-serif;
    font-weight: 700;
    fill: var(--text-light);
  }
  .phone-number {
    font-family: "Stardos Stencil", "Arial Black", sans-serif;
    font-weight: 700;
    fill: var(--text-light);
    letter-spacing: 4px;
  }
</style>
</head>
<body>
<main class="wrap-canvas">
  <svg class="cab-template" viewBox="0 0 1100 470" xmlns="http://www.w3.org/2000/svg" aria-label="Tormelli Welding and Fabrication LLC cab wrap, driver side">
    <defs>
      <clipPath id="cab-body-clip">
        <path id="cab-body-shape" d="M10,200 L35,178 Q100,158 190,150 L380,145 L430,140 L460,108 L630,22 Q830,10 1030,12 Q1068,16 1072,45 L1080,418 Q1078,444 1058,447 L420,455 Q405,440 400,420 Q370,330 250,318 Q120,312 75,380 L55,352 L45,300 L60,262 L28,262 L10,238 Z"/>
      </clipPath>
      <radialGradient id="weld-glow" cx="0.55" cy="0.6" r="0.6">
        <stop offset="0" stop-color="var(--spark-hot)"/>
        <stop offset="0.25" stop-color="var(--spark-warm)" stop-opacity="0.8"/>
        <stop offset="0.6" stop-color="#3a2a1c" stop-opacity="0.6"/>
        <stop offset="1" stop-color="#050505" stop-opacity="0"/>
      </radialGradient>
    </defs>

    <g class="cab-body" clip-path="url(#cab-body-clip)">
      <rect class="base-film" x="0" y="0" width="1100" height="470" fill="var(--wrap-black)"/>

      <g class="welding-visual" role="img" aria-label="Photo of a welding torch throwing sparks onto metal">
        <rect x="160" y="140" width="310" height="210" fill="url(#weld-glow)"/>
      </g>

      <path class="swoosh-white" d="M1016,0 C1012,210 1010,340 905,392 C790,440 600,448 425,462" fill="none" stroke="var(--stripe-white)" stroke-width="9"/>
      <path class="swoosh-orange" d="M988,0 C984,200 986,320 885,368 C770,420 580,432 410,448" fill="none" stroke="var(--accent-orange)" stroke-width="24"/>
    </g>

    <use href="#cab-body-shape" fill="none" stroke="var(--cut-line)" stroke-width="1.6"/>

    <g class="cutouts" fill="var(--paper)">
      <path class="window-front" d="M432,170 L448,148 L470,140 L482,108 Q600,45 722,38 L722,172 Z"/>
      <path class="window-rear" d="M774,36 L960,34 Q968,36 968,48 L970,165 L774,170 Z"/>
      <rect class="hood-vent" x="222" y="184" width="66" height="13" rx="6"/>
      <rect class="handle-front" x="636" y="224" width="74" height="12" rx="5"/>
      <rect class="handle-rear" x="950" y="213" width="70" height="14" rx="6"/>
    </g>

    <g class="brand-block">
      <text class="brand-name" x="646" y="312" text-anchor="middle" font-size="80" textLength="370" lengthAdjust="spacingAndGlyphs">TORMELLI</text>
      <text class="brand-name" x="646" y="346" text-anchor="middle" font-size="22" textLength="370" lengthAdjust="spacingAndGlyphs">WELDING AND FABRICATION LLC</text>
      <text class="phone-number" x="452" y="404" font-size="36" textLength="310" lengthAdjust="spacingAndGlyphs">607.555.0142</text>
    </g>
  </svg>
</main>
</body>
</html>
```